UI design for Fast Food Restaurant Self-Order App

Background:
App purpose: for fast food restaurant customers to self order food/drink by choosing item image, and make payment by tapping the credit card on the card terminal.
Reference: https://www.brivolkiosks.example/product-overview/self-order-kiosks/
Attachment:
Wireframes. (wire frames provide general idea and the information to display, they are not a strict guideline for layout design.)
Tarrowby's Self ordering app.
Intro:
We have built a (for restaurant and cafe) Self Ordering and Payment app, similar to Tarrowby's self ordering software in most of their new restaurants. Our app will be placed in a Quorvane Deskline 10 OS touch screen Kiosk(screen size 4:3 or Portrait 16:9) within the restaurant/cafe premise.
Pages to be designed:
Page 1. Food Browsing Page. displays all food images(to be provided by cafes) by categories, and displays the Cart. This page will lead to Page 2 or Page 3.
'Cart' section should include:
'cart items/selected items', its quantity and price. like Tarrowbys' app.
When click on a Cart Item, we need to allow to change quantity or 'change Choice'. The UI handling these change requests with ease will be one deciding factor for us to choose your design.
Fact: up to 10 food categories, and 10 - 25 food items under each categories.
When click on one item image, it goes to Page 2.
Page 2. Item Detail/Description Page. Shows description of the food, and its available Choice(other food items or Special Request, up to 12) will also be displayed. 'Add item to cart' action(Button Name: ADD) will happen here and go back to Browsing Page 1.
e.g. Item 'Fried Rice' Page. the Choice could be 'Add Egg', 'Add Meat', 'No Chilli' etc.
Page 3. Order Review Page. No edit features allowed on this page, only two buttons: 'No' to go back to Browsing Page, or 'Yes' to proceed to Payment Page 4. Check Tarrowby's screen.
Page 4. Payment Page - Prompt user to Insert or Tap credit card on the credit card terminal. (Exact wording: PLEASE FOLLOW INSTRUCTIONS DISPLAYED ON CREDIT CARD TERMINAL BELOW)
Page 5. Payment status. Successful / Failed.
Our considerations to pick the winner:
1. In terms of design for this task, we look out for page layout, effects, fonts, button style and overall colour scheme. the design should present itself in a clean and modern look, with minimum clicking or scrolling. The app aims to help customers choose and pay for their items quickly.
2.we need to handle both 4:3(as shown in wire frames) and 16:9 screens(like Tarrowby's). there will be a lot more vertical space to utilise when it is in 16:9, resulting less scrolling than 4:3. tell us what you think.
All questions are welcome.
Winner has opportunity to work on a few more app UI. Cheers!
Industry/Entity Type
Fast Food Restaurant
Requirements
Must have
- Button colour differentiation - helps people know what to click next.
- best use of screen space. minimum click and scrolls.
Nice to have
- any personal touch.
Should not have
- unrelated design pattern, e.g. a cute animal or flower pattern in the layout.

```html
<!DOCTYPE html>
<html lang="en">
<head>
<meta charset="UTF-8">
<title>Self-Order Kiosk – Main Dish</title>
<link rel="stylesheet" href="https://fonts.googleapis.com/css2?family=Inter:wght@400;500;600;700&display=swap">
<style>
  :root {
    --sidebar-bg: #404651;
    --content-bg: #f4f4f4;
    --card-bg: #ffffff;
    --accent-blue: #5dd3f8;
    --accent-orange: #ff6a00;
    --text-dark: #1e1e1e;
    --text-muted: #6b6b6b;
    --text-light: #ffffff;
    --brand-square: #5dd3f8;
  }
  * { box-sizing: border-box; margin: 0; padding: 0; }
  html, body {
    width: 1200px; height: 900px; overflow: hidden;
    font-family: "Inter", Arial, sans-serif;
    background: var(--content-bg);
  }
  .kiosk {
    position: relative; width: 1200px; height: 900px;
    display: flex; overflow: hidden;
  }
  .sidebar {
    width: 278px; height: 900px; background: var(--sidebar-bg);
    position: relative; color: var(--text-light);
  }
  .brand {
    position: absolute; top: 40px; left: 0; width: 278px;
    display: flex; flex-direction: column; align-items: center; gap: 18px;
  }
  .brand-square {
    width: 84px; height: 84px; background: var(--brand-square);
  }
  .brand-name {
    font-size: 27px; font-weight: 600; letter-spacing: 2px; color: var(--text-light);
  }
  .menu-title {
    position: absolute; top: 244px; left: 45px;
    font-size: 28px; font-weight: 500;
  }
  .category-list { position: absolute; top: 305px; left: 0; width: 278px; list-style: none; }
  .category-item {
    height: 70px; display: flex; align-items: center; padding-left: 46px;
    font-size: 20px; font-weight: 400;
  }
  .category-item.is-active { background: var(--accent-blue); }
  .orders-button {
    position: absolute; left: 32px; top: 797px; width: 214px; height: 68px;
    background: var(--accent-orange); border-radius: 3px;
    display: flex; align-items: center; justify-content: space-between;
    padding: 0 24px 0 22px; color: var(--text-light); font-size: 20px;
  }
  .orders-count {
    width: 40px; height: 40px; background: var(--card-bg); color: var(--accent-orange);
    border-radius: 4px; display: flex; align-items: center; justify-content: center;
    font-size: 20px;
  }
  .content { flex: 1; position: relative; height: 900px; overflow: hidden; }
  .page-title {
    position: absolute; top: 46px; left: 35px;
    font-size: 28px; font-weight: 400; color: var(--text-dark);
  }
  .food-grid {
    position: absolute; top: 134px; left: 35px;
    display: grid; grid-template-columns: repeat(3, 260px);
    column-gap: 36px; row-gap: 35px;
  }
  .food-card { width: 260px; height: 276px; background: var(--card-bg); }
  .food-photo { width: 260px; height: 196px; }
  .food-info { padding: 12px 18px 0; }
  .food-name { font-size: 17px; color: var(--text-dark); line-height: 22px; }
  .food-price { font-size: 18px; color: var(--text-muted); margin-top: 9px; }
  .photo-burger { background: linear-gradient(160deg, #3a3f44 0%, #a45a2a 55%, #c79b63 100%); }
  .photo-steak { background: linear-gradient(135deg, #7a2b1f 0%, #b5603e 45%, #d9a24c 70%, #6f9a3a 100%); }
  .photo-chicken { background: linear-gradient(150deg, #6d4a24 0%, #b97a35 55%, #e0c08c 100%); }
  .photo-rolls { background: linear-gradient(140deg, #4c8a2e 0%, #d8a052 45%, #e9c27a 100%); }
  .photo-laksa { background: linear-gradient(150deg, #d9502a 0%, #f08a3c 60%, #f3c98a 100%); }
  .photo-platter { background: linear-gradient(160deg, #b8872e 0%, #e3c065 45%, #6e8f4a 100%); }
</style>
</head>
<body>
<div class="kiosk">
  <aside class="sidebar">
    <div class="brand">
      <div class="brand-square"></div>
      <div class="brand-name">RESTAURANT</div>
    </div>
    <h2 class="menu-title">MENU</h2>
    <ul class="category-list">
      <li class="category-item is-active">Main Dish</li>
      <li class="category-item">Christmas</li>
      <li class="category-item">Whole Cakes</li>
      <li class="category-item">Mini Cakes</li>
      <li class="category-item">Add-ons</li>
    </ul>
    <div class="orders-button">
      <span class="orders-label">Your Orders</span>
      <span class="orders-count">3</span>
    </div>
  </aside>

  <main class="content">
    <h1 class="page-title">Main Dish</h1>
    <section class="food-grid">
      <article class="food-card">
        <div class="food-photo photo-burger" role="img" aria-label="Photo of a stacked beef burger on a wooden board"></div>
        <div class="food-info"><p class="food-name">Triple B</p><p class="food-price">USD 20.00</p></div>
      </article>
      <article class="food-card">
        <div class="food-photo photo-steak" role="img" aria-label="Photo of sliced steak with roast potatoes and asparagus"></div>
        <div class="food-info"><p class="food-name">Steak are high</p><p class="food-price">USD 20.00</p></div>
      </article>
      <article class="food-card">
        <div class="food-photo photo-steak" role="img" aria-label="Photo of sliced steak with roast potatoes and asparagus"></div>
        <div class="food-info"><p class="food-name">Food Name</p><p class="food-price">USD 20.00</p></div>
      </article>
      <article class="food-card">
        <div class="food-photo photo-chicken" role="img" aria-label="Photo of fried chicken pieces with bread rolls"></div>
        <div class="food-info"><p class="food-name">Food Name</p><p class="food-price">USD 20.00</p></div>
      </article>
      <article class="food-card">
        <div class="food-photo photo-rolls" role="img" aria-label="Photo of crispy spring rolls with lettuce"></div>
        <div class="food-info"><p class="food-name">Food Name</p><p class="food-price">USD 20.00</p></div>
      </article>
      <article class="food-card">
        <div class="food-photo photo-steak" role="img" aria-label="Photo of sliced steak with roast potatoes and asparagus"></div>
        <div class="food-info"><p class="food-name">Food Name</p><p class="food-price">USD 20.00</p></div>
      </article>
      <article class="food-card">
        <div class="food-photo photo-laksa" role="img" aria-label="Photo of spicy noodle soup with prawns and egg"></div>
        <div class="food-info"><p class="food-name">Food Name</p><p class="food-price">USD 20.00</p></div>
      </article>
      <article class="food-card">
        <div class="food-photo photo-platter" role="img" aria-label="Photo of a sliced meat platter ringed with cucumber"></div>
        <div class="food-info"><p class="food-name">Food Name</p><p class="food-price">USD 20.00</p></div>
      </article>
      <article class="food-card">
        <div class="food-photo photo-steak" role="img" aria-label="Photo of sliced steak with roast potatoes and asparagus"></div>
        <div class="food-info"><p class="food-name">Food Name</p><p class="food-price">USD 20.00</p></div>
      </article>
    </section>
  </main>
</div>
</body>
</html>
```